Covid-19 Mortgage Housing Market Coaching

I need a one page 8.5 x 11 printable infographic to describe the following:
Housing and Mortgage Market Coach
Through your Employer Home-ownership Benefit
The Coronavirus has resulted in an unprecedented Government coordination to reduce the spread of the virus, as such, has altered the way we live and work.
As each of us looks to the potential impact of the Coronavirus to our financial stability, it can be difficult to obtain trusted information to help make sound financial decisions.
As part of your employee home ownership program through your employer, you have access to this educational coaching on the below topics:
• What is happening in the stock market and why it is happening.
• Motivation behind Feds cutting rates and how that translates to the lending market.
• Discuss the future of interest rates.
• Discuss the future of the housing market. How will the spring and summer housing markets be effected?
• Everyone says to refinance now. Is that really in my best interest? Learn how to do a refinance analysis and determine if refinancing is right for you.
Having a better understanding of what is happening in the financial markets, with interest rates and the housing market can help you successfully navigate this rapidly evolving situation.
Please be sure that our phone number is prominently displayed 1-800-555-0182 and our web address www.lanternroofguild.com

```html
<!DOCTYPE html>
<html lang="en">
<head>
<meta charset="utf-8">
<title>Housing and Mortgage Market Coach</title>
<link rel="stylesheet" href="https://fonts.googleapis.com/css2?family=Barlow+Condensed:wght@400;600;700&family=Roboto+Condensed:wght@400;700&family=Archivo+Black&display=swap">
<style>
:root{
  --navy-deep:#0a2340;
  --navy:#163f66;
  --navy-mid:#1d4e7c;
  --green:#6cbf3c;
  --green-light:#8ccf4a;
  --green-dark:#2f9a3e;
  --white:#ffffff;
  --ink:#0d2a48;
  --logo-blue:#1e4a78;
  --photo-a:#9cc6e4;
  --photo-b:#8fae6a;
  --still-a:#e6e2d8;
  --still-b:#c9ad84;
}
*{margin:0;padding:0;box-sizing:border-box}
html,body{width:927px;height:1200px;overflow:hidden;background:var(--white)}
.flyer{position:relative;width:927px;height:1200px;overflow:hidden;
  background:linear-gradient(160deg,var(--navy-mid) 0%,var(--navy) 45%,var(--navy-deep) 100%);
  font-family:"Roboto Condensed",Arial,sans-serif;color:var(--white)}
.header{position:absolute;left:0;top:0;width:927px;height:172px;
  background:linear-gradient(90deg,var(--navy-deep),var(--navy-mid))}
.header__title{position:absolute;left:57px;top:62px;font-family:"Barlow Condensed",sans-serif;
  font-weight:700;font-size:55px;line-height:1;white-space:nowrap}
.header__subtitle{position:absolute;left:57px;top:118px;font-family:"Barlow Condensed",sans-serif;
  font-weight:400;font-size:43px;line-height:1;white-space:nowrap}
.header__rule{position:absolute;left:0;top:170px;width:927px;height:11px;
  background:linear-gradient(90deg,var(--green-light),var(--green-dark))}
.hero-photo{position:absolute;left:0;top:181px;width:927px;height:469px;
  background:linear-gradient(135deg,var(--photo-a),var(--photo-b))}
.brand{position:absolute;left:557px;top:168px;width:300px;height:104px;background:var(--white);
  border-radius:0 0 14px 14px;display:flex;align-items:center;justify-content:center;gap:10px}
.brand__mark{width:22px;height:22px;background:var(--green)}
.brand__text{display:flex;flex-direction:column}
.brand__name{font-weight:700;font-size:19px;color:var(--logo-blue)}
.brand__tag{font-weight:700;font-size:10px;color:var(--logo-blue)}
.intro-banner{position:absolute;left:0;top:563px;width:633px;height:88px;
  background:linear-gradient(90deg,var(--green-dark),var(--green));border-radius:0 12px 0 0;
  padding:6px 30px 0 57px;font-weight:700;font-size:19.5px;line-height:26px}
.body-copy{position:absolute;left:57px;top:670px;width:570px;font-weight:700;font-size:19px;line-height:21px}
.body-copy p{margin-bottom:8px}
.topics{list-style:none;margin-top:14px;padding-left:12px}
.topics li{position:relative;margin-bottom:8px}
.topics li::before{content:"";position:absolute;left:-22px;top:3px;width:14px;height:14px;border-radius:50%;
  background:radial-gradient(circle at 35% 35%,var(--green-light),var(--green-dark))}
.callout{position:absolute;left:646px;top:712px;width:281px;height:180px;
  background:linear-gradient(180deg,var(--green),var(--green-dark));border-radius:12px 0 0 0;
  padding:10px 30px 0 17px;font-family:"Roboto Condensed",sans-serif;font-weight:700;font-size:19px;
  line-height:21px;letter-spacing:-.6px}
.callout-photo{position:absolute;left:646px;top:892px;width:281px;height:140px;
  background:linear-gradient(180deg,var(--still-a),var(--still-b))}
.footer{position:absolute;left:0;top:1030px;width:927px;height:170px}
.footer__band{position:absolute;inset:0}
.footer__cta{position:absolute;left:0;width:927px;text-align:center}
.footer__label{top:48px;font-family:"Archivo Black",sans-serif;font-size:19px;color:var(--ink)}
.footer__phone{top:66px;font-family:"Barlow Condensed",sans-serif;font-weight:700;font-size:48px;color:var(--white);display:flex;justify-content:center;align-items:center;gap:6px}
.footer__web{top:110px;font-family:"Roboto Condensed",sans-serif;font-weight:700;font-size:34px;color:var(--white);display:flex;justify-content:center;align-items:center;gap:12px}
</style>
</head>
<body>
<main class="flyer">
  <header class="header">
    <h1 class="header__title">HOUSING AND MORTGAGE MARKET COACH</h1>
    <p class="header__subtitle">THROUGH YOUR EMPLOYER HOME-OWNERSHIP BENEFIT</p>
  </header>
  <div class="header__rule"></div>

  <div class="hero-photo" role="img" aria-label="Photo of a two-storey suburban house with a garage"></div>

  <div class="brand">
    <span class="brand__mark"></span>
    <div class="brand__text">
      <span class="brand__name">Lantern Roof Guild</span>
      <span class="brand__tag">Employee Home Ownership Program</span>
    </div>
  </div>

  <p class="intro-banner">The Coronavirus has resulted in an unprecedented Government coordination to reduce the spread of the virus, as such, has altered the way we live and work.</p>

  <section class="body-copy">
    <p>As each of us looks to the potential impact of the Coronavirus to our financial stability, it can be difficult to obtain trusted information to help make sound financial decisions.</p>
    <p>As part of your employee home ownership program through your employer, you have access to this educational coaching on the below topics:</p>
    <ul class="topics">
      <li>What is happening in the stock market and why it is happening.</li>
      <li>Motivation behind Feds cutting rates and how that translates to the lending market.</li>
      <li>Discuss the future of interest rates.</li>
      <li>Discuss the future of the housing market. How will the spring and summer housing markets be effected?</li>
      <li>Everyone says to refinance now. Is that really in my best interest? Learn how to do a refinance analysis and determine if refinancing is right for you.</li>
    </ul>
  </section>

  <aside class="callout">Having a better understanding of what is happening in the financial markets, with interest rates and the housing market can help you successfully navigate this rapidly evolving situation.</aside>
  <div class="callout-photo" role="img" aria-label="Photo of a small wooden house model beside stacks of coins"></div>

  <footer class="footer">
    <svg class="footer__band" width="927" height="170" viewBox="0 0 927 170">
      <defs>
        <linearGradient id="band-fill" x1="0" y1="0" x2="1" y2="0">
          <stop offset="0" stop-color="#8ccf4a"/><stop offset="1" stop-color="#2f9a3e"/>
        </linearGradient>
      </defs>
      <polygon points="0,55 463,5 927,55 927,170 0,170" fill="url(#band-fill)"/>
    </svg>
    <div class="footer__cta footer__label">GET STARTED NOW</div>
    <div class="footer__cta footer__phone">
      <svg width="22" height="26" viewBox="0 0 24 24"><path fill="#0d2a48" d="M6.6 10.8a15 15 0 0 0 6.6 6.6l2.2-2.2c.3-.3.7-.4 1-.2 1.1.4 2.3.6 3.6.6.6 0 1 .4 1 1V20c0 .6-.4 1-1 1A17 17 0 0 1 3 4c0-.6.4-1 1-1h3.5c.6 0 1 .4 1 1 0 1.3.2 2.5.6 3.6.1.3 0 .7-.2 1z"/></svg>
      <span>1-800-555-0182</span>
    </div>
    <div class="footer__cta footer__web">
      <svg width="20" height="20" viewBox="0 0 24 24" fill="none" stroke="#0d2a48" stroke-width="2"><circle cx="12" cy="12" r="10"/><path d="M2 12h20M12 2c3 3 3 17 0 20M12 2c-3 3-3 17 0 20"/></svg>
      <span>www.lanternroofguild.com</span>
    </div>
  </footer>
</main>
</body>
</html>
```